VelaMend Wellness Business Cards

I am looking to have luxury business cards made for my IV Therapy and Wellness business.

Target Market(s)

Health and Wellness professionals

Industry/Entity Type

MedSpa

Contact Information for Business Card

Tobin Hargreave, MSN, RN, CCRN Tobin@velamendwellness.com (916) 582-1937 QR code to website www.velamendwellness.com

```html
<!DOCTYPE html>
<html lang="en">
<head>
<meta charset="utf-8">
<title>VelaMend Wellness Business Cards</title>
<link href="https://fonts.googleapis.com/css2?family=Montserrat:wght@400;500;700;800&family=Libre+Baskerville&display=swap" rel="stylesheet">
<style>
  :root {
    --backdrop: #2b2b2d;
    --navy: #201c4f;
    --navy-ink: #2f2a68;
    --sky: #3aa9e0;
    --paper: #ffffff;
    --ink: #1d1d1f;
  }
  * { margin: 0; padding: 0; box-sizing: border-box; }
  html, body {
    width: 1200px; height: 694px; overflow: hidden;
    background: var(--backdrop);
    font-family: "Montserrat", Arial, sans-serif;
  }
  .canvas {
    position: relative; width: 1200px; height: 694px;
    display: flex; align-items: center; justify-content: center; gap: 40px;
  }
  .card {
    width: 540px; height: 309px; border-radius: 22px;
    position: relative; overflow: hidden;
  }
  .card--front { background: var(--navy); display: flex; align-items: center; justify-content: center; }
  .card--back { background: var(--paper); }

  .brand { display: flex; align-items: center; gap: 14px; }
  .brand__dot { width: 22px; height: 22px; border-radius: 50%; background: var(--sky); flex: none; }
  .brand__name { font-weight: 800; letter-spacing: -0.5px; line-height: 1; }
  .card--front .brand__name { color: var(--paper); font-size: 40px; }

  .back-brand { position: absolute; left: 30px; top: 50%; transform: translateY(-50%); gap: 10px; }
  .back-brand .brand__name { color: var(--navy-ink); font-size: 28px; line-height: 1.02; }
  .back-brand .brand__dot { width: 16px; height: 16px; }

  .divider {
    position: absolute; left: 284px; top: 44px; width: 2px; height: 222px;
    background: linear-gradient(to bottom, rgba(47,42,104,0), var(--navy-ink) 30%, var(--navy-ink) 70%, rgba(47,42,104,0));
  }
  .contact { position: absolute; left: 304px; top: 56px; right: 14px; color: var(--ink); }
  .contact__name { font-weight: 800; color: var(--navy-ink); font-size: 20px; letter-spacing: 0.1px; white-space: nowrap; }
  .contact__role { font-family: "Libre Baskerville", Georgia, serif; font-size: 11px; margin-top: 3px; margin-bottom: 16px; }
  .contact__row { display: flex; align-items: center; gap: 8px; font-size: 11px; margin-bottom: 7px; white-space: nowrap; }
  .contact__row svg { width: 13px; height: 13px; flex: none; }
  .contact__address { font-size: 11px; line-height: 1.55; margin-top: 14px; margin-left: 21px; }
</style>
</head>
<body>
<main class="canvas">
  <section class="card card--front" aria-label="Business card front">
    <div class="brand">
      <span class="brand__dot"></span>
      <span class="brand__name">VelaMend Wellness</span>
    </div>
  </section>

  <section class="card card--back" aria-label="Business card back">
    <div class="brand back-brand">
      <span class="brand__dot"></span>
      <span class="brand__name">VelaMend<br>Wellness</span>
    </div>
    <div class="divider"></div>
    <div class="contact">
      <div class="contact__name">Tobin Hargreave</div>
      <div class="contact__role">MSN, RN, CCRN</div>
      <div class="contact__row">
        <svg viewBox="0 0 16 16"><circle cx="8" cy="8" r="8" fill="#3aa9e0"/><path d="M5 4.5c.6-.4 1.2-.3 1.5.3l.6 1.2c.2.4 0 .8-.3 1l-.5.4c.4.9 1 1.6 1.9 2l.4-.5c.3-.3.7-.4 1-.2l1.2.6c.6.3.7.9.3 1.5-.6.8-1.6 1-2.6.5C6.6 10.3 5.7 9.3 4.9 7.4c-.4-1-.6-2.3.1-2.9z" fill="#fff"/></svg>
        <span>(916) 582-1937</span>
      </div>
      <div class="contact__row">
        <svg viewBox="0 0 16 16"><rect x="1" y="3" width="14" height="10" rx="1.5" fill="#3aa9e0"/><path d="M1.5 4l6.5 5 6.5-5" fill="none" stroke="#fff" stroke-width="1.3"/></svg>
        <span>Tobin@velamendwellness.com</span>
      </div>
      <div class="contact__row">
        <svg viewBox="0 0 16 16"><circle cx="8" cy="8" r="7" fill="#3aa9e0"/><g fill="none" stroke="#fff" stroke-width="1"><circle cx="8" cy="8" r="5"/><ellipse cx="8" cy="8" rx="2.2" ry="5"/><path d="M3 8h10"/></g></svg>
        <span>www.velamendwellness.com</span>
      </div>
      <div class="contact__address">421, Address line goes here<br>45452, Country name</div>
    </div>
  </section>
</main>
</body>
</html>
```